Specialist Medical practice after professional trifold flyer design for patient information brochure

I am the Director of the Hollowbrook Clinic, a specialist medial and surgical practice in Australia. I am after a professional design of a patient information trifold flyer that can be used for web distribution or for commercial printing for upcoming educational event. The design would need to allow change of images and text to be used as template for future topics but have a common brand look across them. Colours would follow the logo, but primarily blue colours for the hollowbrook theme. The inside text needs to be clearly contrasted to the background for easy reading, as often elderly patients. The design would make use of curves or circles, but open for hexagonal, triangle square vector components. I have included an outline for the initial brochure and included images to include. Other stock background images can be used if they increase the impact of the design over included. A winning design is also one that could be modified to a 4 page bi-fold brochure

Target Market(s)

This will be provided to patients in GP practices, podiatry clinics, radiological practices. Aimed at patients to read and be compelled to look to site or get consultation with me

Industry/Entity Type

Medical

Font styles to use
Serif
Sans Serif

Colors
33a6d7
0355a3
86cfc6
cedeed
0292cd
85cae6

Requirements
Must have
• The front cover needs to engage the patient to pick up and read- yes I have a painful ankle and want to find out more. the goal for the inside is to provide the options but be able to direct to website for more info - website currently undergoing upgrade. After professional modern look. Not bright contrasting colours like many advertising brochures. Needs to able to have images and text changed but following same look to create new topics
Nice to have
• The focus is a Tri-fold brochure. Nice to be able to modify to bifold. A winning design would even offer both, or submit separate bifold and trifold. I am open to different versions of similar look. (eg option of brochure with curved elements, triangular or square, or hexagonal.
Should not have
• To many contrasting colours. Text must be easily read on background, either white or coloured background texture with transparency

```html
<!DOCTYPE html>
<html lang="en">
<head>
<meta charset="utf-8">
<title>Hollowbrook Clinic – My Painful Ankle trifold</title>
<link rel="stylesheet" href="https://fonts.googleapis.com/css2?family=Open+Sans:wght@400;600;700&family=Ubuntu:wght@400;500;700&family=Russo+One&display=swap">
<style>
:root{
  --board:#a97e55;
  --ice:#cfdff0;
  --paper:#ffffff;
  --mist:#eeeeee;
  --brand:#1d8fd1;
  --brand-deep:#1d62ae;
  --navy:#1f2461;
  --ink:#333333;
  --ink-soft:#555555;
}
*{margin:0;padding:0;box-sizing:border-box}
html,body{width:978px;height:1200px;overflow:hidden}
body{background:var(--board);font-family:"Open Sans",Arial,sans-serif;color:var(--ink);position:relative}
.label{position:absolute;color:#fff;font:400 15px "Open Sans",sans-serif;transform:translateX(-50%)}
.spread{position:absolute;left:72px;width:808px;height:528px;overflow:hidden;box-shadow:0 3px 8px rgba(0,0,0,.35)}
.spread-outside{top:74px}
.spread-inside{top:621px;background:var(--mist)}
.abs{position:absolute}
.photo{position:absolute}

/* back cover */
.back-cover{left:0;top:0;width:404px;height:528px;background:var(--ice)}
.profile-card{left:25px;top:26px;width:202px;height:400px}
.profile-name{left:25px;top:44px;width:202px;text-align:center;color:#fff;font:500 18px Ubuntu,sans-serif}
.profile-cred{left:25px;top:72px;width:202px;text-align:center;color:#fff;font:400 9.5px/14px "Open Sans",sans-serif}
.profile-bio{left:36px;top:104px;width:180px;color:#fff;font:400 6.6px/10.4px "Open Sans",sans-serif;text-align:justify}
.doctor-photo{left:50px;top:180px;width:160px;height:178px;background:linear-gradient(180deg,#2d9fe0 0%,#3a6ea0 45%,#1c2838 100%);border-radius:80px 80px 0 0}
.badge-circle{left:84px;top:358px;width:72px;height:72px;border-radius:50%;background:#fff;box-shadow:0 2px 5px rgba(0,0,0,.25)}
.brand-mark{display:flex;align-items:center;gap:6px;white-space:nowrap}
.brand-dot{width:24px;height:24px;border-radius:50%;background:var(--brand-deep);flex:none}
.brand-name{font:700 12.5px Ubuntu,sans-serif;color:var(--brand-deep);letter-spacing:.2px}
.brand-tag{font:400 5px "Open Sans",sans-serif;color:var(--brand-deep);letter-spacing:.8px;margin-top:1px}
.section-title{color:var(--brand-deep);font:500 11.5px Ubuntu,sans-serif}
.intro-bold{font:700 6.4px/8.4px "Open Sans",sans-serif;color:var(--ink)}
.tick-list{list-style:none}
.tick-list li{position:relative;padding-left:10px;font:400 6.3px/8px "Open Sans",sans-serif;color:var(--ink-soft);margin-bottom:4px}
.tick-list li::before{content:"";position:absolute;left:0;top:1px;width:6px;height:6px;border-radius:50%;background:var(--brand-deep)}
.dot-list{list-style:none}
.dot-list li{position:relative;padding-left:10px;font:400 7.2px/12.6px "Open Sans",sans-serif;color:var(--ink)}
.dot-list li::before{content:"";position:absolute;left:0;top:3px;width:6.5px;height:6.5px;border-radius:50%;background:var(--brand)}
.locations-bar{left:20px;top:442px;width:364px;height:13px;background:#f3f6fb;text-align:center;font:400 8.5px/13px "Open Sans",sans-serif;letter-spacing:2px;color:var(--ink)}
.loc{top:462px;font:400 6.3px/8.6px "Open Sans",sans-serif;color:var(--ink-soft)}
.loc-rule{top:460px;width:1px;height:36px;background:#9bb0c8}
.loc-contact{left:262px;top:462px;font:600 7.8px/13px "Open Sans",sans-serif;color:var(--ink)}
.web-band{left:0;top:503px;width:404px;height:25px;background:var(--brand);color:#fff;text-align:center;font:700 8.5px/25px "Open Sans",sans-serif;letter-spacing:4.5px}

/* front cover */
.front-cover{left:404px;top:0;width:404px;height:528px;background:var(--paper)}
.cover-photo{left:0;top:0;width:404px;height:290px;background:linear-gradient(160deg,#8a5a36 0%,#d9a467 35%,#e8c78e 55%,#8f8a3e 80%,#5f6a2e 100%)}
.headline{right:28px;top:28px;text-align:right;color:var(--navy);font:400 38px/37px "Russo One",sans-serif}
.headline-sub{right:28px;top:154px;text-align:right;color:var(--navy);font:400 26px/26px "Russo One",sans-serif}
.web-pill{left:22px;top:271px;width:196px;height:22px;border-radius:11px 11px 11px 0;background:var(--brand-deep);color:#fff;font:700 11px/22px "Open Sans",sans-serif;text-align:center}
.cover-intro{left:20px;top:308px;width:364px;font:400 6.2px/9.5px "Open Sans",sans-serif;color:var(--ink)}
.cover-intro b{color:var(--brand-deep);font-weight:400}
.thumb{top:334px;width:117px;height:80px}
.cover-caption{left:22px;top:425px;width:300px;font:400 5.6px/8px "Open Sans",sans-serif;color:var(--ink)}
.cover-name{left:22px;top:455px;color:var(--brand-deep);font:500 16.5px Ubuntu,sans-serif}
.cover-role{left:22px;top:478px;color:var(--ink-soft);font:400 7.8px "Open Sans",sans-serif}
.cover-contact{left:22px;top:500px;color:var(--ink-soft);font:400 14px "Open Sans",sans-serif}
.cover-contact strong{color:var(--brand-deep);font:700 15px Ubuntu,sans-serif}
.cover-brand{left:214px;top:460px}
.cover-email{right:20px;top:506px;font:600 7px "Open Sans",sans-serif;color:var(--ink)}

/* front inside */
.intro-col{left:26px;top:29px;width:218px;font:400 6.3px/8.4px "Open Sans",sans-serif;color:var(--ink-soft)}
.intro-col p{margin-bottom:8px;text-align:justify}
.xray-inline{float:right;width:120px;height:136px;margin:0 0 4px 6px;background:radial-gradient(ellipse at 55% 55%,#d8d8d8 0%,#8a8a8a 35%,#2a2a2a 75%)}
.conditions-box{left:260px;top:29px;width:124px;height:286px;background:var(--brand);padding:6px 8px;color:#fff}
.conditions-box h3{font:400 13px/14px "Russo One",sans-serif;margin-bottom:6px}
.conditions-box .intro-bold{color:#fff;margin-bottom:4px}
.conditions-box .tick-list li{color:#fff}
.conditions-box .tick-list li::before{background:#fff}
.building-photo{left:0;bottom:0;width:124px;height:96px;background:linear-gradient(180deg,#e9eef3 0%,#b9c3cc 40%,#3b4148 70%,#2f5a2c 100%)}
.inside-photo{left:0;top:336px;width:404px;height:192px;background:linear-gradient(160deg,#0e2a48 0%,#2a5d8f 35%,#d99a6c 60%,#e9dccf 100%)}
.inside-title{left:27px;top:449px;font:700 20px/24px Ubuntu,sans-serif}
.inside-title .lt{color:#fff}
.inside-title .dk{color:#3a3a3a}

/* back inside */
.topic{left:422px;width:238px}
.topic h2{color:var(--brand-deep);font:500 14px Ubuntu,sans-serif;margin-bottom:6px}
.topic p{font:400 6.2px/8.3px "Open Sans",sans-serif;color:var(--ink);text-align:justify;margin-bottom:7px}
.xray{left:670px;width:114px;background:radial-gradient(ellipse at 50% 50%,#dcdcdc 0%,#8d8d8d 30%,#2b2b2b 70%,#1a1a1a 100%)}
.closing-band{left:404px;top:336px;width:404px;height:192px;background:linear-gradient(120deg,#1e8fd0 0%,#126aa8 45%,#0b2f52 100%)}
.results-box{left:422px;top:282px;width:238px;height:134px;background:var(--brand);padding:9px 10px;color:#fff}
.results-box h2{font:500 13.5px Ubuntu,sans-serif;margin-bottom:6px}
.results-box p{font:400 6.2px/8.9px "Open Sans",sans-serif;text-align:justify}
.closing-title{left:422px;top:432px;color:#fff;font:700 18px Ubuntu,sans-serif}
.closing-sub{left:422px;top:462px;color:#fff;font:700 20px/25px Ubuntu,sans-serif}
.closing-rule{left:586px;top:431px;width:1px;height:76px;background:rgba(255,255,255,.7)}
.closing-name{left:602px;top:428px;color:#fff;font:500 15.5px Ubuntu,sans-serif}
.closing-role{left:602px;top:449px;color:#fff;font:400 7.4px "Open Sans",sans-serif}
.closing-hr{left:602px;top:464px;width:140px;height:1px;background:rgba(255,255,255,.4)}
.closing-phone{left:602px;top:470px;color:#fff;font:500 18px Ubuntu,sans-serif}
.closing-email{left:602px;top:497px;color:#fff;font:600 8px "Open Sans",sans-serif}
</style>
</head>
<body>

<div class="label" style="left:270px;top:41px">Back Cover</div>
<div class="label" style="left:674px;top:41px">Front Cover</div>

<section class="spread spread-outside">
  <!-- back cover -->
  <div class="abs back-cover">
    <svg class="abs profile-card" viewBox="0 0 202 400" width="202" height="400" aria-hidden="true">
      <path d="M10 0H192Q202 0 202 10V330Q202 340 190 344L120 372Q101 380 82 372L12 344Q0 340 0 330V10Q0 0 10 0Z" fill="#1d8fd1"/>
    </svg>
    <div class="abs profile-name">Dr Marcus Ellery</div>
    <div class="abs profile-cred">MBBS (UCA), FRACS (Ortho)<br>FA (Ortho)</div>
    <p class="abs profile-bio">Dr Marcus Ellery is an Australian trained Orthopaedic Surgeon who has a primary focus in the treatment of conditions of the foot and ankle. He has completed post fellowship training in Foot and Ankle surgery both locally and internationally, and continues to update himself in the latest techniques.</p>
    <div class="photo doctor-photo" role="img" aria-label="Portrait of the surgeon in suit and tie"></div>
    <div class="abs badge-circle"></div>

    <div class="abs" style="left:242px;top:44px">
      <div class="brand-mark"><span class="brand-dot"></span><div><div class="brand-name">HOLLOWBROOK CLINIC</div><div class="brand-tag">MEDICAL &amp; SURGICAL SPECIALISTS</div></div></div>
    </div>

    <div class="abs" style="left:242px;top:102px;width:148px">
      <h3 class="section-title">CONDITIONS TREATED</h3>
      <p class="intro-bold" style="margin:8px 0 8px">Dr Ellery provides assessment and treatment of all foot and ankle conditions. He has special interest in the following:</p>
      <ul class="tick-list">
        <li>Minimally invasive treatment for bunions and toe deformities.</li>
        <li>Joint sparing procedures for arthritis or deformity, including the Flexa implant.</li>
        <li>Joint fusion procedures for arthritis of the feet and ankle</li>
        <li>Sports injuries and tendinopathies.</li>
        <li>Total ankle replacement and deformity correction of the foot and ankle.</li>
      </ul>
    </div>

    <div class="abs" style="left:242px;top:266px;width:150px">
      <h3 class="section-title" style="margin-bottom:4px">Foot &amp; Ankle</h3>
      <ul class="dot-list">
        <li>Bunions, Hammer toes</li>
        <li>Arthritis</li>
        <li>Ligament, tendon injuries</li>
        <li>Joint arthroscopy</li>
        <li>Minimally Invasive surgery</li>
        <li>Ankle replacement, fusion</li>
        <li>Chronic ankle instability</li>
        <li>Flexa Implant</li>
      </ul>
    </div>

    <div class="abs locations-bar">OUR LOCATIONS</div>
    <p class="abs loc" style="left:23px">Suite 402, Level 4<br>Kestrel Private Hospital<br>88 Marlin St, Wollongong NSW</p>
    <div class="abs loc-rule" style="left:170px"></div>
    <p class="abs loc" style="left:181px;top:467px;line-height:12px">14 Quarry Road,<br>Nowra NSW</p>
    <div class="abs loc-rule" style="left:250px"></div>
    <p class="abs loc-contact">Fax : (02) 4000 7312<br>info@hollowbrookclinic.com.au</p>
    <div class="abs web-band">www.hollowbrookclinic.com.au</div>
  </div>

  <!-- front cover -->
  <div class="abs front-cover">
    <div class="photo cover-photo" role="img" aria-label="Runner holding a painful ankle in a sunlit field"></div>
    <h1 class="abs headline">MY<br>PAINFUL<br>ANKLE</h1>
    <div class="abs headline-sub">SOLUTIONS<br>FOR ANKLE<br>ARTHRITIS</div>
    <div class="abs web-pill">www.hollowbrookclinic.com.au</div>
    <p class="abs cover-intro">Hollowbrook Clinic located on Level 4 of the Kestrel Private Hospital. <b>Our Clinic provides comprehensive Orthopaedic, Neurosurgical, Neurological, Pain Management and Rehabilitation Services</b> to the Illawarra and South Coast Region.</p>
    <div class="photo thumb" style="left:22px;background:linear-gradient(180deg,#bcd6ee 0%,#eef3f8 50%,#3c4550 80%,#2d4a26 100%)" role="img" aria-label="Hospital building exterior"></div>
    <div class="photo thumb" style="left:141px;background:linear-gradient(180deg,#f3f5f8 0%,#dfe6ee 60%,#9db4cc 100%)" role="img" aria-label="Doctor reviewing an x-ray"></div>
    <div class="photo thumb" style="left:260px;background:linear-gradient(160deg,#f2f6fa 0%,#c8d8e8 50%,#2f5f94 100%)" role="img" aria-label="Stethoscope resting on a keyboard"></div>
    <p class="abs cover-caption">The Hollowbrook Clinic is a specialist medical and surgical practice offering comprehensive diagnosis and treatment in orthopaedic, neurosurgical, neurological and rehabilitation conditions.</p>
    <div class="abs cover-name">Dr Marcus Ellery</div>
    <div class="abs cover-role">Orthopaedic Foot and Ankle Surgeon</div>
    <div class="abs cover-contact">CONTACT: <strong>(02) 4000 7311</strong></div>
    <div class="abs cover-brand">
      <div class="brand-mark"><span class="brand-dot" style="width:28px;height:28px"></span><div><div class="brand-name" style="font-size:13.5px">HOLLOWBROOK CLINIC</div><div class="brand-tag" style="font-size:5.5px">MEDICAL &amp; SURGICAL SPECIALISTS</div></div></div>
    </div>
    <div class="abs cover-email">Email: info@hollowbrookclinic.com.au</div>
  </div>
</section>

<section class="spread spread-inside">
  <!-- front inside -->
  <div class="abs intro-col">
    <p>Ankle arthritis is a painful condition where there is loss of cartilage from the ankle joint surface. Although not as common as knee or hip arthritis, pain can be debilitating affecting quality of life.</p>
    <p>Arthritis of the joint can be caused by trauma joint such as fracture or recurrent instability or secondary from inflammatory conditions such as rheumatoid arthritis.</p>
    <p>Pain from the joint will occur with activity causing a limp, limiting walking speed and distance. Often there is swelling of the joint with progressive loss of motion.</p>
    <p>Diagnosis is made with examination of the ankle and weight bearing x-rays showing loss of joint space.</p>
    <div class="xray-inline" role="img" aria-label="Side x-ray of an arthritic ankle"></div>
    <p>When pain medication, activity modification and shoe ware modification is no longer effective to control the pain then then it is worthwhile discussing with your GP for referral to Dr Marcus Ellery for an opinion on further treatment. As an Orthopaedic Foot and Ankle surgeon, he will be able to assess your conditions and give advice on the best options for your treatment.</p>
    <p style="clear:both">The decision on the best option is based on your age, activity level, existing medical problems, previous ankle treatment and your expected outcome from treatment. In the situation of end stage arthritis options consist of either Ankle fusion or Total Ankle replacement.</p>
  </div>

  <div class="abs conditions-box">
    <h3>CONDITIONS<br>TREATED</h3>
    <p class="intro-bold">Dr Ellery provides assessment and treatment of all foot and ankle conditions. He has special interest in the following:</p>
    <ul class="tick-list">
      <li>Minimally invasive treatment for bunions and toe deformities.</li>
      <li>Joint sparing procedures for arthritis or deformity, including the Flexa implant.</li>
      <li>Joint fusion procedures for arthritis of the feet and ankle</li>
      <li>Sports injuries and tendinopathies.</li>
      <li>Total ankle replacement and deformity correction of the foot and ankle.</li>
    </ul>
    <div class="photo building-photo" role="img" aria-label="Hospital building exterior"></div>
  </div>

  <div class="photo inside-photo" role="img" aria-label="Runner's leg with the ankle bones highlighted"></div>
  <div class="abs inside-title"><span class="lt">My Painful Ankle</span><br><span class="dk">Ankle Arthritis</span></div>

  <!-- back inside -->
  <div class="abs closing-band"></div>

  <article class="abs topic" style="top:29px">
    <h2>Ankle Fusion Surgery</h2>
    <p>This operation aims to stiffen the ankle joint by fusing the tibia and talus together in the optimal position for function. The common thought is that there will be no movement of the foot, and the patient will walk with a limp.</p>
    <p>The fusion only occurs at the ankle joint, leaving motion available to the surrounding joints. Although there is decreased motion, you will walk more normally after a fusion without a limp as the pain to the joint is removed.</p>
    <p>For more information on ankle fusion, risks and recovery visit our website:<br><b>www.hollowbrookclinic.com.au/Ankle-Fusion</b></p>
  </article>

  <article class="abs topic" style="top:150px">
    <h2>Total Ankle Replacement Surgery</h2>
    <p>In suitable patients there may be the option to maintain joint motion and perform a Total Ankle Replacement. Like a hip or knee replacement operation, the arthritic joint is removed and replaced with an artificial joint. Like an ankle fusion there will alleviation of the pain and limp with maintenance of the ankle joint motion. Recovery to walking post-surgery is often much sooner than with ankle fusion. Dr Marcus Ellery if one of the few surgeons to have completed an international fellowship in ankle replacement surgery and has been performing the technique since 2008. He is currently performing the technique using the Horizon Total ankle with Compass guides.</p>
    <p>For more information on ankle fusion, risks and recovery visit our website<br><b>www.hollowbrookclinic.com.au/Ankle-Replacement</b></p>
  </article>

  <div class="photo xray" style="top:19px;height:160px" role="img" aria-label="X-ray of a fused ankle with plate and screws"></div>
  <div class="photo xray" style="top:185px;height:132px" role="img" aria-label="X-ray of a total ankle replacement"></div>

  <div class="abs results-box">
    <h2>Results of surgery</h2>
    <p>Successful surgery in the suitable patient will help resolve the pain associated with the ankle arthritis. Ankle Fusion surgery is ideal for patients with heavy labour work, allowing them to return to previous activities. There may be the risk of arthritis to surrounding joints in the future, but often this occurs many years down the track. Results from Total Ankle replacement surgery have been improving over the years, but there is known risks of loosening, cyst formation or failure of the joint over time that can occur in some patients. It is important to have a opinion from an Orthopaedic Foot and Ankle Surgeon experienced in the these procedure to determine which procedure will provide the best long term solution for you.</p>
  </div>

  <div class="abs closing-title">My Painful Ankle</div>
  <div class="abs closing-sub">Solutions For<br>Ankle Arthritis</div>
  <div class="abs closing-rule"></div>
  <div class="abs closing-name">Dr Marcus Ellery</div>
  <div class="abs closing-role">Orthopaedic Foot and Ankle Surgeon</div>
  <div class="abs closing-hr"></div>
  <div class="abs closing-phone">(02) 4000 7311</div>
  <div class="abs closing-email">info@hollowbrookclinic.com.au</div>
</section>

<div class="label" style="left:262px;top:1157px">Front Inside</div>
<div class="label" style="left:662px;top:1157px">Back Inside</div>

</body>
</html>
```